Business Card For Kelmora Financial Consulting

Hi, I would like a business card designed. Bold, modern.
Please use the same design as the logo. I have also attached the website design to see the overall theme.
Wordmark Font
Color: Hex: #01AEF7

```html
<!DOCTYPE html>
<html lang="en">
<head>
<meta charset="utf-8">
<title>Kelmora Financial Consulting — Business Card</title>
<link rel="stylesheet" href="https://fonts.googleapis.com/css2?family=Montserrat:wght@500;700;800&family=Nunito+Sans:wght@400;600&display=swap">
<style>
  :root {
    --stage: #1c2229;
    --card: #ffffff;
    --navy: #0b4068;
    --navy-deep: #0a3556;
    --sky: #01aef7;
    --sky-soft: #35a6e0;
    --ink: #2d3137;
  }
  * { box-sizing: border-box; margin: 0; padding: 0; }
  html, body {
    width: 1200px; height: 900px; overflow: hidden;
    background: var(--stage);
  }
  .stage {
    width: 1200px; height: 900px;
    display: flex; align-items: center; justify-content: center;
  }
  .card {
    position: relative;
    width: 900px; height: 514px;
    background: var(--card);
    overflow: hidden;
    box-shadow: 0 20px 50px rgba(0,0,0,.45);
    font-family: "Nunito Sans", sans-serif;
    color: var(--ink);
  }
  .card__swoosh {
    position: absolute; inset: 0;
    width: 100%; height: 100%;
  }
  .brand {
    position: absolute; left: 70px; top: 150px;
    display: flex; align-items: center; gap: 16px;
  }
  .brand__square {
    width: 34px; height: 34px;
    background: var(--sky);
  }
  .brand__name {
    font-family: "Montserrat", sans-serif;
    font-weight: 800;
    font-size: 25px;
    letter-spacing: 1px;
    text-transform: uppercase;
    color: var(--navy);
    line-height: 1.15;
    width: 270px;
  }
  .divider {
    position: absolute; left: 430px; top: 120px;
    width: 2px; height: 190px;
    background: var(--navy);
  }
  .contact {
    position: absolute; left: 462px; top: 122px;
  }
  .contact__name {
    font-family: "Montserrat", sans-serif;
    font-weight: 800;
    font-size: 30px;
    color: var(--navy);
    text-transform: uppercase;
    letter-spacing: .5px;
  }
  .contact__title {
    font-size: 20px;
    color: var(--sky-soft);
    margin-top: 0;
  }
  .contact__address {
    font-size: 19px; line-height: 1.3;
    margin-top: 14px;
  }
  .contact__line {
    display: flex; align-items: center; gap: 8px;
    font-size: 19px; line-height: 1.35;
  }
  .contact__line:first-of-type { margin-top: 8px; }
  .contact__icon { width: 16px; height: 16px; flex: none; }
  .card__web {
    position: absolute; right: 56px; bottom: 22px;
    font-size: 21px; font-weight: 600;
    color: #ffffff;
    letter-spacing: .3px;
  }
</style>
</head>
<body>
<main class="stage">
  <article class="card">
    <svg class="card__swoosh" viewBox="0 0 900 514" preserveAspectRatio="none" aria-hidden="true">
      <path d="M0 318 C 250 350, 520 400, 900 440 L900 514 L0 514 Z" fill="var(--sky-soft)"/>
      <path d="M0 336 C 260 372, 520 420, 900 452 L900 514 L0 514 Z" fill="#ffffff"/>
      <path d="M0 346 C 260 385, 520 428, 900 458 L900 514 L0 514 Z" fill="var(--sky-soft)"/>
      <path d="M0 360 C 260 400, 520 436, 900 462 L900 514 L0 514 Z" fill="var(--navy)"/>
    </svg>

    <div class="brand">
      <span class="brand__square"></span>
      <span class="brand__name">Kelmora Financial Consulting</span>
    </div>

    <span class="divider"></span>

    <section class="contact">
      <h1 class="contact__name">Maren Tolvik</h1>
      <p class="contact__title">President</p>
      <p class="contact__address">1180 Harbor Crest Dr<br>Seacliff CA 92041</p>
      <p class="contact__line">
        <svg class="contact__icon" viewBox="0 0 24 24" aria-hidden="true"><path fill="var(--sky)" d="M6.6 10.8a15.1 15.1 0 0 0 6.6 6.6l2.2-2.2a1 1 0 0 1 1-.25 11.4 11.4 0 0 0 3.6.57 1 1 0 0 1 1 1V20a1 1 0 0 1-1 1A17 17 0 0 1 3 4a1 1 0 0 1 1-1h3.5a1 1 0 0 1 1 1c0 1.25.2 2.45.57 3.57a1 1 0 0 1-.25 1z"/></svg>
        555-014-2298
      </p>
      <p class="contact__line">
        <svg class="contact__icon" viewBox="0 0 24 24" aria-hidden="true"><path fill="var(--sky)" d="M2 5h20v14H2z M2 5l10 8 10-8" stroke="#fff" stroke-width="1.5"/></svg>
        info@KelmoraConsulting.com
      </p>
    </section>

    <p class="card__web">www.KelmoraConsulting.com</p>
  </article>
</main>
</body>
</html>
```